依頼詳細
健康食品のパッケージデザイン(紙製化粧箱)です。底面のテキストはデザインは必要ありませんので、添付ファイルにて後日お知らせします。パッケージ仕様、その他詳細は添付ファイルをご覧ください。多くの方のご提案をお待ちしております。
記載項目
W58mm×D58mm×H204mm(紙箱)
希望イメージ
シンプル 複雑
単色 カラフル
暗い 明るい
日常 高級
遊び心 厳粛
未来的 伝統的
女性的 男性的
希望する色
グレー系
納品ファイル
• 高解像度JPG (.jpg)
• イラストレーター形式 (.ai)
補足説明
パッケージ型と底面テキストは後日添付いたします。
記載項目「パッケージサイズ」を訂正して、パッケージ型を添付します。
パッケージサイズW140mm×D65mm×H100mm
どうぞよろしくお願いしします。
■ 選んだ理由

複数提案すべてイメージ通りでした。対応も丁寧で迅速です。ありがとうございます。

■ 提案者全員のお礼・コメント

多くのご提案ありがとうございました。次の機会もぜひよろしくお願いします。

```html
<!DOCTYPE html>
<html lang="ja">
<head>
<meta charset="utf-8">
<title>Valora 化粧箱 展開図</title>
<link rel="stylesheet" href="https://fonts.googleapis.com/css2?family=Noto+Sans+JP:wght@400;500&family=Noto+Serif+JP:wght@500&display=swap">
<style>
  :root {
    --paper: #ffffff;
    --board: #4b4b4d;
    --crease: #bdbdbd;
    --accent: #c8313a;
    --ink-light: #e9e9e9;
    --label-tone: #a25a6a;
  }
  html, body {
    margin: 0;
    padding: 0;
    width: 875px;
    height: 1200px;
    overflow: hidden;
    background: var(--paper);
  }
  .dieline {
    display: block;
    width: 875px;
    height: 1200px;
  }
  .panel { fill: var(--board); stroke: var(--crease); stroke-width: 0.6; stroke-linejoin: round; }
  .fold { fill: none; stroke: var(--crease); stroke-width: 0.35; }
  .accent-line { fill: none; stroke: var(--accent); stroke-width: 0.7; }
  .brand-name {
    font-family: "Noto Sans JP", sans-serif;
    font-weight: 500;
    font-size: 8px;
    letter-spacing: 0.6px;
    fill: var(--ink-light);
  }
  .brand-dot { fill: var(--ink-light); }
  .tagline {
    font-family: "Noto Serif JP", serif;
    font-weight: 500;
    font-size: 6.2px;
    letter-spacing: 0.8px;
    fill: var(--ink-light);
  }
  .spec-text {
    font-family: "Noto Sans JP", sans-serif;
    font-size: 2.3px;
    fill: var(--ink-light);
  }
  .product-label { fill: var(--label-tone); }
</style>
</head>
<body>
<svg class="dieline" viewBox="0 0 300 411.4" xmlns="http://www.w3.org/2000/svg">
  <!-- top tuck flap -->
  <path class="panel" d="M104 22 L108 6 L192 6 L196 22 L198 48 L102 48 Z"/>
  <line class="fold" x1="102" y1="22" x2="198" y2="22"/>

  <!-- top dust panel and main body -->
  <path class="panel" d="M64 62 L72 48 L228 48 L236 62 L240 62 L240 340 L60 340 L60 62 Z"/>
  <line class="fold" x1="60" y1="62" x2="240" y2="62"/>
  <line class="fold" x1="102" y1="48" x2="102" y2="62"/>
  <line class="fold" x1="198" y1="48" x2="198" y2="62"/>
  <line class="fold" x1="60" y1="195" x2="240" y2="195"/>
  <line class="fold" x1="60" y1="62" x2="102" y2="100"/>
  <line class="fold" x1="240" y1="62" x2="198" y2="100"/>
  <line class="fold" x1="102" y1="100" x2="102" y2="195"/>
  <line class="fold" x1="198" y1="100" x2="198" y2="195"/>
  <line class="fold" x1="60" y1="195" x2="102" y2="160"/>
  <line class="fold" x1="240" y1="195" x2="198" y2="160"/>

  <!-- left side flap -->
  <path class="panel" d="M60 74 L20 74 L20 78 L6 82 L6 158 L20 162 L20 166 L60 166 Z"/>
  <line class="fold" x1="20" y1="78" x2="20" y2="162"/>
  <line class="fold" x1="44" y1="74" x2="44" y2="166"/>

  <!-- right side flap -->
  <path class="panel" d="M240 74 L280 74 L280 78 L294 82 L294 158 L280 162 L280 166 L240 166 Z"/>
  <line class="fold" x1="280" y1="78" x2="280" y2="162"/>
  <line class="fold" x1="256" y1="74" x2="256" y2="166"/>

  <!-- bottom flap -->
  <path class="panel" d="M102 340 L198 340 L198 396 L192 406 L108 406 L102 396 Z"/>
  <line class="fold" x1="102" y1="380" x2="198" y2="380"/>

  <!-- separate strip -->
  <rect class="panel" x="40" y="214" width="60" height="182"/>
  <line class="fold" x1="40" y1="250" x2="100" y2="250"/>
  <line class="fold" x1="40" y1="292" x2="100" y2="292"/>
  <line class="fold" x1="40" y1="346" x2="100" y2="346"/>

  <!-- accent lines -->
  <polyline class="accent-line" points="62,76 86,98 86,120"/>
  <polyline class="accent-line" points="238,76 214,98 214,120"/>
  <polyline class="accent-line" points="122,272 206,252 238,252"/>

  <!-- back panel information -->
  <text class="spec-text" transform="translate(118 118) rotate(90)">保存方法表示</text>
  <rect class="product-label" x="112" y="134" width="10" height="18" role="img" aria-label="商品ラベル写真"/>
  <g class="spec-text">
    <text x="128" y="72">名称：栄養補助食品 内容量：60粒</text>
    <text x="128" y="104">原材料：植物性エキス、ビタミン類</text>
    <text x="128" y="108">保存方法：高温多湿を避けて保存</text>
    <text x="128" y="122">栄養成分表示</text>
    <text x="128" y="134">お召し上がり方：一日二粒を目安に</text>
    <text x="128" y="138">水またはぬるま湯でお飲みください</text>
    <text x="128" y="150">販売者：株式会社サンプル</text>
    <text x="128" y="160">お問い合わせ窓口</text>
  </g>

  <!-- front panel -->
  <text class="brand-name" x="104" y="246">Valora</text>
  <circle class="brand-dot" cx="140" cy="243.2" r="2.8"/>
  <path class="fold" d="M138 296 L138 288 L162 288 L162 296"/>
  <text class="tagline" x="108" y="322">輝きある毎日へ</text>
</svg>
</body>
</html>
```